Marrowby's Vacation Rentals Business Card

Multi Million dollar villa rentals in the Dominican Republic.

Industry/Entity Type

Business

Contact Information for Business Card

I am looking for a high-end look around my company name/logo (see attached) on one side incorporating the following info: first and last name, title, address, phone #, email and company website. On the backside I want to add a full color picture of one of our villas (see attached).

```html
<!DOCTYPE html>
<html lang="en">
<head>
<meta charset="utf-8">
<title>Marrowby's Vacation Rentals – Business Card</title>
<link rel="stylesheet" href="https://fonts.googleapis.com/css2?family=Open+Sans:wght@400;600;700&display=swap">
<style>
  :root {
    --bg: #e9e6e1;
    --card: #ffffff;
    --orange: #f47b20;
    --ink: #1e1e1e;
    --photo-top: #8fb7e3;
    --photo-bottom: #e4e1da;
  }
  * { margin: 0; padding: 0; box-sizing: border-box; }
  html, body { width: 1200px; height: 900px; overflow: hidden; }
  body {
    background: var(--bg);
    font-family: "Open Sans", Arial, sans-serif;
    color: var(--ink);
    position: relative;
  }
  .card {
    position: absolute;
    left: 250px;
    width: 700px;
    height: 400px;
    background: var(--card);
    box-shadow: 0 4px 14px rgba(0,0,0,0.18);
    overflow: hidden;
  }
  .card--front { top: 40px; }
  .card--back { top: 460px; }

  .front-graphics { position: absolute; inset: 0; width: 700px; height: 400px; }

  .holder { position: absolute; left: 100px; top: 26px; }
  .holder__name { font-size: 22px; font-weight: 700; color: var(--orange); line-height: 1.1; }
  .holder__title { font-size: 14px; font-weight: 400; line-height: 1.3; }

  .contact { position: absolute; left: 118px; top: 140px; list-style: none; }
  .contact__item { display: flex; align-items: center; gap: 10px; font-size: 17px; line-height: 26px; white-space: nowrap; }
  .contact__icon { width: 14px; height: 14px; flex: none; }

  .address { position: absolute; left: 118px; top: 232px; font-size: 17px; line-height: 24px; font-style: normal; white-space: nowrap; }

  .brand { position: absolute; left: 380px; top: 168px; display: flex; align-items: center; gap: 10px; }
  .brand__mark { width: 30px; height: 30px; border-radius: 50%; background: var(--orange); flex: none; }
  .brand__name { font-size: 29px; font-weight: 700; color: var(--ink); line-height: 1.15; white-space: nowrap; }

  .villa-photo {
    position: absolute; inset: 0;
    background: linear-gradient(160deg, var(--photo-top) 0%, var(--photo-bottom) 100%);
  }
</style>
</head>
<body>

<section class="card card--front" aria-label="Business card front">
  <svg class="front-graphics" viewBox="0 0 700 400" aria-hidden="true">
    <polygon points="0,0 52,0 30,32 0,32" fill="var(--orange)"/>
    <polygon points="58,0 90,0 60,60 28,60" fill="var(--ink)"/>
    <polygon points="0,300 290,322 278,348 0,326" fill="var(--orange)"/>
    <polygon points="300,336 700,366 700,400 280,400 280,370" fill="var(--ink)"/>
  </svg>

  <div class="holder">
    <p class="holder__name">Daniel Harrow</p>
    <p class="holder__title">Managing Director</p>
  </div>

  <ul class="contact">
    <li class="contact__item">
      <svg class="contact__icon" viewBox="0 0 14 14"><path d="M3 1l2 3-1.3 1.3a8 8 0 0 0 5 5L10 9l3 2-1.5 2.5C6 13 1 8 .5 2.5z" fill="var(--orange)"/></svg>
      044-123 456 789
    </li>
    <li class="contact__item">
      <svg class="contact__icon" viewBox="0 0 14 14"><rect x="1" y="3" width="12" height="8" fill="var(--orange)"/><path d="M1 3l6 5 6-5" stroke="#fff" stroke-width="1.2" fill="none"/></svg>
      info@webname.com
    </li>
    <li class="contact__item">
      <svg class="contact__icon" viewBox="0 0 14 14"><path d="M6 8l2-2M5 6L3 8a2 2 0 0 0 3 3l2-2M9 8l2-2a2 2 0 0 0-3-3L6 5" stroke="var(--orange)" stroke-width="1.6" fill="none" stroke-linecap="round"/></svg>
      www.websitename.com
    </li>
  </ul>

  <address class="address">
    12345, Address Goes Here<br>
    Country Name, 123456.
  </address>

  <div class="brand">
    <span class="brand__mark" aria-hidden="true"></span>
    <p class="brand__name">Marrowby's<br>Vacation Rentals</p>
  </div>
</section>

<section class="card card--back" aria-label="Business card back">
  <div class="villa-photo" role="img" aria-label="Full colour photograph of one of the company's villas"></div>
</section>

</body>
</html>
```